VORLEN Website Design

We need a website designed for our company VORLEN. We are a luxury lifestyle club that will provide benefits and services for our members. The site should be clean & sleek, preferably using black and white (or darker colors). (example sites: brimvale.example, tusko.example)

Here is a link of a sample page I did using wix. (https://pelmundry4.sitebuild.example/mypage) This can be used to get a general idea.

Target Market(s)

Upper Middle Class in the United States

Number of Pages Required

5+ page

Font styles to use
Sans Serif
Other font styles liked:
• Arial (or other similar fonts)

Requirements
Must have
• A clean design that is eye-catching and speaks to our company.
Nice to have
• Ideas for copy.

```html
<!DOCTYPE html>
<html lang="en">
<head>
<meta charset="UTF-8">
<title>VORLEN — A Members Only Lifestyle Club</title>
<link href="https://fonts.googleapis.com/css2?family=Poppins:wght@300;400;500;700;800&family=Great+Vibes&display=swap" rel="stylesheet">
<style>
  :root {
    --accent: #14afd6;
    --accent-deep: #0f8fb0;
    --ink: #222222;
    --ink-soft: #3a3a3a;
    --paper: #f2f2f2;
    --white: #ffffff;
    --night: #0c0c0c;
    --panel: #333333;
  }
  * { box-sizing: border-box; margin: 0; padding: 0; }
  html, body { width: 754px; height: 1200px; overflow: hidden; }
  body { font-family: 'Poppins', Arial, sans-serif; color: var(--ink); position: relative; background: var(--white); }
  .abs { position: absolute; }

  /* Hero */
  .hero { position: absolute; left: 0; top: 0; width: 754px; height: 357px;
    background: radial-gradient(ellipse at 50% 45%, #6b5a4c 0%, #3b322c 45%, #1c1a19 100%); }
  .hero-photo { position: absolute; inset: 0; }
  .topbar { position: absolute; left: 0; top: 0; width: 754px; height: 38px; background: rgba(20,20,20,0.55); }
  .brand { position: absolute; left: 16px; top: 7px; font-size: 22px; font-weight: 500; color: var(--white); letter-spacing: 0.5px; }
  .nav { position: absolute; top: 13px; font-size: 10px; font-weight: 500; color: var(--white); }
  .nav-sep { position: absolute; top: 13px; font-size: 10px; color: rgba(255,255,255,0.5); }
  .nav-active::after { content: ""; position: absolute; left: 0; right: 0; bottom: -8px; height: 2px; background: var(--accent); }
  .join-top { position: absolute; left: 646px; top: 0; width: 108px; height: 38px; background: var(--accent); color: var(--white);
    font-size: 9.5px; font-weight: 500; display: flex; align-items: center; justify-content: center; }
  .hero-title { position: absolute; left: 0; width: 754px; top: 142px; text-align: center; font-family: 'Great Vibes', cursive;
    font-size: 32px; color: var(--white); }
  .hero-sub { position: absolute; left: 0; width: 754px; top: 187px; text-align: center; font-size: 13px; font-weight: 300; color: var(--white); }
  .btn { position: absolute; background: var(--accent); color: var(--white); font-size: 9px; font-weight: 500;
    display: flex; align-items: center; justify-content: center; }

  /* About */
  .about { position: absolute; left: 0; top: 357px; width: 754px; height: 264px; background: var(--paper); }
  .about-photo { position: absolute; left: 146px; top: 33px; width: 248px; height: 199px;
    background: radial-gradient(circle at 30% 25%, #e0b060 0%, #8a6434 30%, #3a2a1e 75%, #221a14 100%); }
  .about-label { position: absolute; left: 362px; top: 48px; width: 94px; height: 38px; background: var(--panel); color: var(--white);
    padding: 2px 6px; line-height: 1; }
  .about-label .small { font-size: 14px; font-weight: 700; display: block; }
  .about-label .big { font-size: 21px; font-weight: 700; display: block; margin-top: 1px; }
  .about-copy { position: absolute; left: 406px; top: 100px; width: 210px; font-size: 9px; line-height: 11.3px; color: var(--ink-soft); }
  .about-copy p + p { margin-top: 9px; }

  /* Services */
  .services { position: absolute; left: 0; top: 621px; width: 754px; height: 342px;
    background: linear-gradient(90deg, #2a2a2c 0%, #1a1a1b 45%, #080808 62%, #000 100%); }
  .services-title { position: absolute; left: 30px; top: 98px; font-size: 22px; font-weight: 800; color: var(--white); letter-spacing: 0.2px; }
  .services-title .amp { color: var(--accent); }
  .services-copy { position: absolute; left: 30px; top: 151px; width: 280px; font-size: 9px; line-height: 11.2px; color: #e6e6e6; }
  .services-copy p + p { margin-top: 11px; }
  .tile { position: absolute; width: 104px; }
  .tile-img { width: 104px; height: 64px; }
  .tile-label { margin-top: 5px; text-align: center; font-size: 9.5px; color: var(--white); }

  /* Interest */
  .interest { position: absolute; left: 0; top: 963px; width: 754px; height: 194px; background: var(--accent); }
  .interest-title { position: absolute; left: 0; width: 754px; top: 30px; text-align: center; font-size: 24px; font-weight: 800; color: var(--white); }
  .interest-copy { position: absolute; left: 150px; width: 454px; top: 68px; text-align: center; font-size: 9.3px; line-height: 11.2px; color: var(--white); }
  .field { position: absolute; background: var(--accent-deep); color: #e8f7fb; font-size: 9.5px; padding-left: 5px; display: flex; align-items: center; }
  .submit { position: absolute; left: 434px; top: 118px; width: 100px; height: 43px; background: var(--white); color: var(--accent);
    font-size: 9px; font-weight: 700; display: flex; align-items: center; justify-content: center; }

  /* Footer */
  .footer { position: absolute; left: 0; top: 1157px; width: 754px; height: 43px; background: var(--white); }
  .foot-links { position: absolute; left: 146px; top: 7px; font-size: 9.5px; font-weight: 500; color: var(--ink); display: flex; align-items: center; gap: 9px; }
  .dot { width: 3px; height: 3px; border-radius: 50%; background: var(--accent); }
  .copyright { position: absolute; left: 146px; top: 27px; font-size: 6.5px; color: #666; }
  .social { position: absolute; left: 465px; top: 0; width: 143px; height: 43px; background: var(--panel);
    display: flex; align-items: center; justify-content: center; gap: 15px; }
  .social span { width: 16px; height: 16px; border-radius: 50%; background: var(--white); }
</style>
</head>
<body>

<header class="hero">
  <div class="hero-photo" role="img" aria-label="Friends celebrating with drinks at a lively club party"></div>
  <div class="topbar">
    <div class="brand">VORLEN</div>
    <div class="nav nav-active" style="left:236px">Home</div>
    <div class="nav-sep" style="left:277px">|</div>
    <div class="nav" style="left:293px">About</div>
    <div class="nav-sep" style="left:335px">|</div>
    <div class="nav" style="left:350px">Services and Benefits</div>
    <div class="nav-sep" style="left:464px">|</div>
    <div class="nav" style="left:479px">Contact</div>
    <div class="join-top">JOINT CLUBE</div>
  </div>
  <h1 class="hero-title">A Members Only Lifestyle Club</h1>
  <div class="hero-sub">BECOME A MEMBER TODAY!</div>
  <div class="btn" style="left:338px;top:217px;width:79px;height:27px">JOINT CLUBE</div>
</header>

<section class="about">
  <div class="about-photo" role="img" aria-label="Guests toasting with champagne glasses under warm bokeh lights"></div>
  <div class="about-label"><span class="small">About</span><span class="big">VORLEN</span></div>
  <div class="about-copy">
    <p>VORLEN is a members only lifestyle club founded in order to bring the best services, experiences, and opportunities to our diverse community of members.</p>
    <p>Our members consist of creatives, athletes, artists, and other professionals.</p>
  </div>
  <div class="btn" style="left:406px;top:191px;width:70px;height:18px">READ MORE</div>
</section>

<section class="services">
  <div class="abs" style="left:0;top:0;width:380px;height:342px" role="img" aria-label="Travellers walking a red carpet from a private jet at dusk"></div>
  <h2 class="services-title">SERVICES <span class="amp">&amp;</span> BENEFITS</h2>
  <div class="services-copy">
    <p>Built in the image of a"Multi-Family Office", VORLEN provides members with access to just about any service, experience, and event desirable.</p>
    <p>VORLEN is truly the most exclusive lifestyle club out there.</p>
  </div>
  <div class="btn" style="left:30px;top:219px;width:70px;height:18px">APPLY</div>

  <div class="tile" style="left:382px;top:33px"><div class="tile-img" role="img" aria-label="Pen over financial charts" style="background:linear-gradient(135deg,#dfe6ee,#9fb3c8)"></div><div class="tile-label">Accounting</div></div>
  <div class="tile" style="left:505px;top:33px"><div class="tile-img" role="img" aria-label="Rising investment line chart" style="background:linear-gradient(135deg,#2b4f9a,#142a5e)"></div><div class="tile-label">Investment</div></div>
  <div class="tile" style="left:626px;top:33px"><div class="tile-img" role="img" aria-label="Lawyer in suit holding a book" style="background:linear-gradient(135deg,#7a3a2a,#1e1e24)"></div><div class="tile-label">Lawyer</div></div>

  <div class="tile" style="left:382px;top:133px"><div class="tile-img" role="img" aria-label="Couple receiving house keys" style="background:linear-gradient(135deg,#3f7fc2,#c9b89a)"></div><div class="tile-label">Real Estate</div></div>
  <div class="tile" style="left:505px;top:133px"><div class="tile-img" role="img" aria-label="Concierge desk with picture frame" style="background:linear-gradient(135deg,#f4f1ec,#c7b9a6)"></div><div class="tile-label">24/7 Concierge</div></div>
  <div class="tile" style="left:626px;top:133px"><div class="tile-img" role="img" aria-label="Passengers beside a private jet" style="background:linear-gradient(180deg,#dfe8f0,#b0a89a)"></div><div class="tile-label">Private Jet Travel</div></div>

  <div class="tile" style="left:382px;top:232px"><div class="tile-img" role="img" aria-label="Black and white event crowd" style="background:linear-gradient(135deg,#d8d8d8,#2a2a2a)"></div><div class="tile-label">Event Access</div></div>
  <div class="tile" style="left:505px;top:232px"><div class="tile-img" role="img" aria-label="Group dinner party at a table" style="background:linear-gradient(135deg,#8a6a52,#3c4a3a)"></div><div class="tile-label">Private Events</div></div>
  <div class="tile" style="left:626px;top:232px"><div class="tile-img" role="img" aria-label="Diver swimming with a manta ray" style="background:linear-gradient(180deg,#3fa9d6,#0b4f7a)"></div><div class="tile-label">Experiences</div></div>
</section>

<section class="interest">
  <h2 class="interest-title">INDICATION OF INTEREST</h2>
  <p class="interest-copy">Hey - Thanks for your interest! We will begin accepting applications in 2019. In the meantime, simply fill out the indication of interest below and we will be in touch once we begin accepting applications!</p>
  <div class="field" style="left:220px;top:118px;width:208px;height:18px">Full Name</div>
  <div class="field" style="left:220px;top:143px;width:100px;height:18px">Email</div>
  <div class="field" style="left:327px;top:143px;width:101px;height:18px">Phone</div>
  <div class="submit">SUBMIT</div>
</section>

<footer class="footer">
  <nav class="foot-links">
    <span>Home</span><i class="dot"></i><span>About</span><i class="dot"></i><span>Services &amp; Benefits</span><i class="dot"></i><span>Contact</span>
  </nav>
  <div class="copyright">Copyright © 2018 VORLEN. All Rights Reserved.</div>
  <div class="social" aria-label="Social links"><span></span><span></span><span></span><span></span></div>
</footer>

</body>
</html>
```